QRV Consulting Web Design… We need a Facelift!

We currently have a website but it is very outdated. We like our content, but could use some help on giving it a refreshed facelift.

www.QRV-Consulting.example is our site

We only consult with large companies in the US that have sales over $250,000 a year, so looking to be high end yet approachable in our look.

Target Market(s)

Large corporations

Industry/Entity Type

Consulting

Coding

Coded - Design and coding required

Number of Pages Required

5+ page

Font styles to use
Serif
Sans Serif

Requirements
Must have
• We love our logo, keep that the same.
• The site colors can deviate from the logo, as long as it is complimentary
Nice to have
• We like our videos and graphics. If you can make them better, then great! But you can also feel free to reuse them.
• There is a video on the opening screen and one on the video page.
• We would like the video on the video page to be incorporated on the first page.
• If you think we need other/more page, we are all ears!
Should not have
• Want to set us apart from our competition in look, feel, professionalism and step away from the old fashioned conservatives of their websites. We want to be professional, yet bolder and fresher.
• Our Competition is LedgerPilot.example and TheBrindlewoodGroup.example, but not looking to copy of emulate them, but gives an idea of the world QRV is in.

```html
<!DOCTYPE html>
<html lang="en">
<head>
<meta charset="utf-8">
<title>QRV Consulting</title>
<link href="https://fonts.googleapis.com/css2?family=Signika:wght@400;600&family=Raleway:ital,wght@0,400;0,500;0,600;1,400&display=swap" rel="stylesheet">
<style>
:root{
  --red:#9b0a0f;
  --red-bright:#c4161c;
  --blue:#5b8fd6;
  --blue-light:#8fb3ea;
  --ink:#2b2b2b;
  --text:#444;
  --grey-bg:#ededed;
  --client-bg:#e9eef3;
  --footer:#1d1d1d;
  --white:#fff;
}
*{box-sizing:border-box;margin:0;padding:0}
html,body{width:1200px;height:2659px;overflow:hidden}
body{font-family:"Raleway",Arial,sans-serif;color:var(--text);background:var(--white);position:relative}
.accent{color:var(--red)}
.section-title{position:absolute;left:0;width:1200px;text-align:center;font-family:"Signika",Arial,sans-serif;font-weight:400;font-size:35px;color:var(--ink)}
.title-bar{position:absolute;left:50%;transform:translateX(-50%);width:40px;height:3px;background:var(--red-bright)}
.title-rule{position:absolute;left:50%;transform:translateX(-50%);width:300px;height:1px;background:linear-gradient(90deg,transparent,#ccc,transparent)}

/* header */
.site-header{position:absolute;top:0;left:0;width:1200px;height:154px;background:linear-gradient(#fafafa,#e6e6e6)}
.top-line{position:absolute;top:0;left:0;width:1200px;height:4px;background:var(--blue)}
.brand{position:absolute;left:124px;top:44px;width:240px}
.brand-name{display:block;font-family:"Signika",Arial,sans-serif;font-size:32px;font-weight:600;color:#555;line-height:38px}
.brand-site{display:block;font-family:"Raleway",Arial,sans-serif;font-size:14px;font-weight:600;color:#555;margin-top:14px}
.call-bar{position:absolute;top:9px;left:684px;height:36px;display:flex;align-items:center;gap:10px;font-size:15px;color:#444;font-weight:500}
.call-icon{width:30px;height:30px;border-radius:50%;background:#fff;border:1px solid #ddd;display:flex;align-items:center;justify-content:center}
.social{display:flex;gap:8px;margin-left:10px}
.social span{width:24px;height:24px;border-radius:50%;display:block}
.main-nav{position:absolute;left:381px;top:50px;width:819px;height:74px;background:linear-gradient(#b0151a,var(--red));border-radius:37px 0 0 37px;display:flex;align-items:center;padding-left:40px}
.main-nav a{color:#fff;text-decoration:none;font-size:14px;font-weight:500;text-transform:uppercase;width:125px;text-align:center}

/* slider */
.hero{position:absolute;top:154px;left:0;width:1200px;height:534px;background:linear-gradient(135deg,#3e4868 0%,#2f3854 45%,#4a5066 100%)}
.hero-table{position:absolute;left:660px;top:0;width:540px;height:534px;background:linear-gradient(150deg,#c9bfb0,#8e8a84 70%,transparent);opacity:.35}
.hero-caption{position:absolute;left:0;top:213px;width:585px;height:136px;background:linear-gradient(90deg,rgba(255,255,255,.92),rgba(255,255,255,.75) 70%,rgba(255,255,255,0))}
.hero-caption p{position:absolute;left:101px;top:14px;font-family:"Signika",Arial,sans-serif;font-size:31px;line-height:37px;color:var(--red);white-space:nowrap}
.slide-arrow{position:absolute;top:264px;width:40px;height:40px;border-radius:50%;background:#fff;display:flex;align-items:center;justify-content:center;box-shadow:0 1px 4px rgba(0,0,0,.4)}

/* welcome */
.welcome h2{position:absolute;left:99px;top:718px;font-family:"Signika",Arial,sans-serif;font-weight:400;font-size:35px;color:var(--ink)}
.welcome .underline{position:absolute;left:99px;top:770px;width:578px;height:1px;background:#ccc}
.welcome .underline::before{content:"";position:absolute;left:0;top:-1px;width:118px;height:3px;background:var(--red)}
.welcome p{position:absolute;left:99px;top:783px;width:580px;font-size:13px;line-height:23.5px;color:#333}
.btn{position:absolute;left:99px;top:922px;width:117px;height:39px;background:linear-gradient(#b5161c,var(--red));color:#fff;font-size:13px;display:flex;align-items:center;justify-content:center;border-radius:3px}
.video{position:absolute;left:707px;top:727px;width:392px;height:239px;border-radius:6px;padding:6px;background:#fff;box-shadow:0 0 6px rgba(0,0,0,.3)}
.video-frame{width:100%;height:190px;background:linear-gradient(120deg,#c7d3df,#6f8398 55%,#1f2c3d);position:relative}
.play{position:absolute;left:50%;top:50%;width:46px;height:46px;margin:-23px;border-radius:50%;background:rgba(255,255,255,.85);display:flex;align-items:center;justify-content:center}
.video-controls{height:31px;background:#111;display:flex;align-items:center;gap:12px;padding:0 10px;color:#ddd;font-size:11px}
.progress{flex:1;height:7px;background:#444;border-radius:4px;position:relative}
.progress::after{content:"";position:absolute;left:55px;top:-3px;width:13px;height:13px;border-radius:50%;background:#ccc}

/* why */
.why{position:absolute;top:993px;left:0;width:1200px;height:460px;background:linear-gradient(120deg,#8ea1b8 0%,#5c7392 35%,#31486c 70%,#25375a 100%)}
.why .section-title{top:22px;color:#fff}
.feature{position:absolute;width:412px;height:99px;background:#fff;border-radius:50px;box-shadow:0 2px 6px rgba(0,0,0,.35)}
.feature .icon{position:absolute;top:11px;width:77px;height:77px;border-radius:50%;display:flex;align-items:center;justify-content:center}
.feature h3{position:absolute;top:16px;font-size:15px;font-weight:500;color:#333}
.feature p{position:absolute;top:41px;width:250px;font-size:13px;line-height:22px;color:#555}
.feature.left .icon{left:13px}.feature.left h3,.feature.left p{left:108px}
.feature.right .icon{right:13px}.feature.right h3,.feature.right p{right:108px;text-align:right}
.feature h3.hot{color:var(--red-bright)}
.icon.red{background:radial-gradient(#b3151a,#7e070b)}
.icon.grey{background:radial-gradient(#8a8a8a,#555)}
.more{color:var(--red-bright);font-weight:600}
.why-hub{position:absolute;left:457px;top:120px;width:284px;height:284px;border-radius:50%;background:rgba(255,255,255,.55);display:flex;align-items:center;justify-content:center}
.why-hub-inner{width:252px;height:252px;border-radius:50%;background:#fff;display:flex;flex-direction:column;align-items:center;justify-content:center;box-shadow:0 2px 8px rgba(0,0,0,.3)}
.why-hub .brand-name{font-size:26px;line-height:30px}
.why-hub .brand-site{font-size:13px;margin-top:6px}

/* process */
.process .section-title{top:1491px}
.step{position:absolute;top:1614px;width:260px;text-align:center}
.step-ring{margin:0 auto;width:130px;height:130px;border-radius:50%;background:#fff;border:8px solid var(--red-bright);display:flex;align-items:center;justify-content:center;box-shadow:0 4px 8px rgba(0,0,0,.25)}
.step h3{font-family:"Signika",Arial,sans-serif;font-weight:400;font-size:23px;color:var(--red-bright);margin-top:17px}
.step ul{list-style:none;font-size:12.5px;line-height:19.5px;color:#333;margin-top:4px}
.dots{position:absolute;top:1665px;display:flex;align-items:center;gap:19px}
.dots i{display:block;border-radius:50%;background:#ddd}

/* testimonials */
.testimonials{position:absolute;top:1891px;left:0;width:1200px;height:319px;background:var(--grey-bg)}
.testimonials .section-title{top:26px}
.avatar{position:absolute;top:134px;width:86px;height:86px;border-radius:50%;border:3px solid #fff;background:radial-gradient(circle at 50% 40%,#d7a57f,#8a4f2e 70%);box-shadow:0 1px 4px rgba(0,0,0,.3)}
.quote{position:absolute;top:130px;width:370px;height:102px;background:#fff;box-shadow:0 1px 4px rgba(0,0,0,.2);padding:14px 18px 0 36px;font-size:12px;font-style:italic;line-height:18px;color:#666;text-align:center}
.quote::before{content:"\201C";position:absolute;left:10px;top:0;font-size:38px;color:#ccc;font-style:normal}
.quote::after{content:"";position:absolute;left:-10px;top:40px;border:10px solid transparent;border-left:0;border-right-color:#fff}
.attribution{position:absolute;top:262px;font-size:13px;color:#333;text-align:center;width:370px}

/* clients */
.clients{position:absolute;top:2210px;left:0;width:1200px;height:277px;background:var(--client-bg)}
.clients .section-title{top:36px}
.client{position:absolute;top:139px;width:165px;height:70px;background:#fff;display:flex;align-items:center;justify-content:center;gap:8px;font-size:22px;font-weight:600;color:#333}
.client .mark{width:18px;height:18px;border-radius:50%;background:#333}
.client-arrow{position:absolute;top:164px;width:22px;height:22px;background:#111;border-radius:4px;display:flex;align-items:center;justify-content:center}

/* newsletter */
.newsletter{position:absolute;top:2487px;left:0;width:1200px;height:62px;background:linear-gradient(#a5121a,#820a0f)}
.newsletter .label{position:absolute;left:155px;top:18px;color:#fff;font-size:18px;font-family:"Signika",Arial,sans-serif}
.newsletter .envelope{position:absolute;left:101px;top:14px}
.email{position:absolute;left:328px;top:16px;width:327px;height:32px;background:#e18f8f;border:1px solid #c85a5a;font-size:12px;color:#6a2020;padding:9px 10px}
.subscribe{position:absolute;left:672px;top:16px;width:112px;height:32px;background:#f2f2f2;color:#222;font-size:12px;font-weight:600;display:flex;align-items:center;justify-content:center}
.follow{position:absolute;left:832px;top:16px;display:flex;align-items:center;gap:10px;color:#fff;font-size:19px;font-family:"Signika",Arial,sans-serif}
.follow span{width:26px;height:26px;border-radius:50%;display:block;border:2px solid #fff}

/* footer */
.site-footer{position:absolute;top:2549px;left:0;width:1200px;height:110px;background:var(--footer)}
.footer-icons{position:absolute;left:101px;top:36px;display:flex;gap:4px}
.footer-icons span{width:40px;height:40px;border-radius:50%;display:flex;align-items:center;justify-content:center}
.footer-brand{position:absolute;left:200px;top:43px;font-family:"Signika",Arial,sans-serif;font-size:22px;font-weight:600;color:#999}
.footer-nav{position:absolute;left:486px;top:34px;display:flex;font-size:13px;color:#ddd}
.footer-nav a{color:#ddd;text-decoration:none;padding:0 23px;border-left:1px solid #444}
.footer-nav a:first-child{border-left:0}
.copyright{position:absolute;right:97px;top:75px;font-size:12px;color:#ccc}
</style>
</head>
<body>

<header class="site-header">
  <div class="top-line"></div>
  <div class="brand"><span class="brand-name">QRV Consulting</span><span class="brand-site">QRV-Consulting.example</span></div>
  <div class="call-bar">
    <span class="call-icon"><svg width="14" height="14" viewBox="0 0 24 24"><path fill="#c4161c" d="M6.6 10.8a15 15 0 0 0 6.6 6.6l2.2-2.2c.3-.3.7-.4 1-.2 1.1.4 2.3.6 3.6.6.6 0 1 .4 1 1V20c0 .6-.4 1-1 1A17 17 0 0 1 3 4c0-.6.4-1 1-1h3.5c.6 0 1 .4 1 1 0 1.3.2 2.5.6 3.6.1.3 0 .7-.2 1z"/></svg></span>
    CALL US NOW : 0100 555 010
    <span class="social"><span style="background:#3b5b9a"></span><span style="background:#2ba3e0"></span><span style="background:#1f7bb5"></span><span style="background:#d34836"></span></span>
  </div>
  <nav class="main-nav">
    <a>Home</a><a>About Us</a><a>Why QRV?</a><a>Our Process</a><a>Client</a><a>Contact Us</a>
  </nav>
</header>

<section class="hero" role="img" aria-label="Photo from above of business people meeting around a conference table with laptop and papers">
  <div class="hero-table"></div>
  <div class="hero-caption"><p>Introducing A Brand-new Way<br>To Manage Your Treasury<br>Management Fees</p></div>
  <span class="slide-arrow" style="left:38px"><svg width="12" height="14" viewBox="0 0 12 14"><path d="M9 1 3 7l6 6" fill="none" stroke="#222" stroke-width="2.5"/></svg></span>
  <span class="slide-arrow" style="left:1121px"><svg width="12" height="14" viewBox="0 0 12 14"><path d="m3 1 6 6-6 6" fill="none" stroke="#222" stroke-width="2.5"/></svg></span>
</section>

<section class="welcome">
  <h2>Welcome <span class="accent">QRV Consulting</span></h2>
  <div class="underline"></div>
  <p>Lorem ipsum dolor sit amet, consectetuer adipiscing elit, sed diam nonummy ni euismod tincidunt ut laoreet dolore magna aliquam erat volutpat. Ut wisi enim ad minim venia quis n dolore eu feugiat nulla facilisis at vero eros et accumsan et iusto oditincidunt ut laoreet dolore magna aliquam erat volutpat. Ut wisi enim ad minim veniam, quis o digniss Lorem duis dolore te feugait nulla facilisi...</p>
  <span class="btn">Read More</span>
  <div class="video">
    <div class="video-frame" role="img" aria-label="Video still of a businessman using a tablet at a desk">
      <span class="play"><svg width="16" height="18" viewBox="0 0 16 18"><path d="M2 1l13 8-13 8z" fill="#333"/></svg></span>
    </div>
    <div class="video-controls">
      <svg width="10" height="12" viewBox="0 0 10 12"><path d="M0 0l10 6-10 6z" fill="#ddd"/></svg>
      <span>04:59</span><span class="progress"></span><span>10:35</span>
      <svg width="14" height="12" viewBox="0 0 14 12"><path d="M0 4h3l4-4v12L3 8H0z" fill="#ddd"/></svg>
      <svg width="12" height="12" viewBox="0 0 12 12"><path d="M1 11 11 1M7 1h4v4M1 7v4h4" fill="none" stroke="#ddd" stroke-width="1.6"/></svg>
    </div>
  </div>
</section>

<section class="why" role="img" aria-label="Blurred background photo of a businessman in suit and tie at a desk with laptop">
  <h2 class="section-title">Why <span style="color:#c4161c">QRV?</span></h2>
  <div class="title-bar" style="top:80px"></div>

  <div class="feature left" style="left:101px;top:159px">
    <span class="icon red"><svg width="40" height="34" viewBox="0 0 40 34"><path d="M4 32h6V22H4zm9 0h6V16h-6zm9 0h6V10h-6zm9 0h6V4h-6z" fill="#fff"/><path d="M3 17 15 8l7 4L36 2" fill="none" stroke="#fff" stroke-width="2"/></svg></span>
    <h3 class="hot">Profitability</h3>
    <p>Clients enjoy gains they neverthought possible by looking ... <span class="more">[+]</span></p>
  </div>
  <div class="feature left" style="left:101px;top:287px">
    <span class="icon grey"><svg width="40" height="36" viewBox="0 0 40 36"><circle cx="20" cy="12" r="9" fill="none" stroke="#fff" stroke-width="2.5"/><circle cx="20" cy="10" r="3" fill="#fff"/><path d="M2 30c8-6 14 2 22-2l8-4" fill="none" stroke="#fff" stroke-width="3"/></svg></span>
    <h3>Insiders</h3>
    <p>Our team has managed treasury personnel as well as client... <span class="more">[+]</span></p>
  </div>
  <div class="feature right" style="left:691px;top:159px">
    <span class="icon grey"><svg width="42" height="30" viewBox="0 0 42 30"><path d="M2 12l10-8 8 4 6-3 14 8-12 12-6-4-6 5-6-6z" fill="#fff"/></svg></span>
    <h3>Involved</h3>
    <p>Clients enjoy gains never possible <span class="more">[+]</span> .. before, with millions of dollars</p>
  </div>
  <div class="feature right" style="left:691px;top:287px">
    <span class="icon grey"><svg width="34" height="38" viewBox="0 0 34 38"><path d="M4 2h20l6 6v28H4z" fill="#fff"/><path d="M9 14h16M9 20h16M9 26h10" stroke="#666" stroke-width="2"/></svg></span>
    <h3>Thorough</h3>
    <p>A complete turn-key solution. We <span class="more">[+]</span> ...do the work, you make the</p>
  </div>

  <div class="why-hub"><div class="why-hub-inner"><span class="brand-name">QRV Consulting</span><span class="brand-site">QRV-Consulting.example</span></div></div>
</section>

<section class="process">
  <h2 class="section-title">Our <span class="accent">Process</span></h2>
  <div class="title-rule" style="top:1555px"></div>
  <div class="title-bar" style="top:1551px"></div>

  <div class="step" style="left:93px">
    <div class="step-ring"><svg width="46" height="40" viewBox="0 0 46 40"><g fill="#222"><circle cx="16" cy="22" r="11"/><circle cx="34" cy="10" r="7"/><circle cx="34" cy="31" r="6"/></g><g stroke="#222" stroke-width="4"><path d="M16 8v28M2 22h28M6 12l20 20M26 12 6 32"/></g><g fill="#fff"><circle cx="16" cy="22" r="4"/><circle cx="34" cy="10" r="2.5"/><circle cx="34" cy="31" r="2"/></g></svg></div>
    <h3>Model</h3>
    <ul><li>Bullet Gather statements</li><li>Bullet Analyze against market</li><li>Bullet Calculate profitability</li></ul>
  </div>
  <div class="dots" style="left:333px"><i style="width:9px;height:9px"></i><i style="width:13px;height:13px"></i><i style="width:19px;height:19px"></i><i style="width:28px;height:28px"></i></div>
  <div class="step" style="left:466px">
    <div class="step-ring"><svg width="56" height="34" viewBox="0 0 56 34"><path d="M2 6h8l8-4 10 4 8-4h10l8 4v14l-14 12-8-6-6 6-10-10H2z" fill="#222"/><path d="M20 12l8 6 6-4" fill="none" stroke="#fff" stroke-width="2"/></svg></div>
    <h3>Engage</h3>
    <ul><li>Review win-win strategies</li><li>Bullet Discuss with providers</li><li>Bullet Finalize agreements</li></ul>
  </div>
  <div class="dots" style="left:713px"><i style="width:9px;height:9px"></i><i style="width:13px;height:13px"></i><i style="width:19px;height:19px"></i><i style="width:28px;height:28px"></i></div>
  <div class="step" style="left:847px">
    <div class="step-ring"><svg width="44" height="44" viewBox="0 0 44 44"><path d="M4 2h20l6 6v30H4z" fill="#222"/><path d="M8 12h14M8 18h10M8 24h10" stroke="#fff" stroke-width="2"/><circle cx="26" cy="26" r="8" fill="#fff" stroke="#222" stroke-width="3"/><path d="M32 32l9 9" stroke="#222" stroke-width="4"/></svg></div>
    <h3>Audit</h3>
    <ul><li>Inspect pricing adherence</li><li>Bullet Continue market benchmarking</li><li>Bullet Complete contract compliance</li></ul>
  </div>
</section>

<section class="testimonials">
  <h2 class="section-title">What <span class="accent">People Say</span></h2>
  <div class="title-rule" style="top:90px"></div>
  <div class="title-bar" style="top:86px"></div>

  <div class="avatar" role="img" aria-label="Portrait photo of a treasurer" style="left:99px"></div>
  <div class="quote" style="left:197px">"In the 20 years I've been in treasury management, I really felt that I'd mastered our bank pricing. But when Istarted understanding bank's profitability so that I could laser focus on line items or rates for discussion, it became a game changer."</div>
  <div class="attribution" style="left:190px">Treasurer of a National Retail Department Store</div>

  <div class="avatar" role="img" aria-label="Portrait photo of a chief financial officer" style="left:631px"></div>
  <div class="quote" style="left:730px">"The last thing we need to do is upset the lending relationship we have with our banks. Employing a mutually beneficial approach in negotiating rates and fees was critical to our long-term success."</div>
  <div class="attribution" style="left:725px;top:259px">CFO of a National Healthcare Company</div>
</section>

<section class="clients">
  <h2 class="section-title">Our <span class="accent">Client</span></h2>
  <div class="title-bar" style="top:96px"></div>
  <span class="client-arrow" style="left:50px"><svg width="8" height="10" viewBox="0 0 8 10"><path d="M7 0v10L0 5z" fill="#fff"/></svg></span>
  <div class="client" style="left:101px"><span class="mark"></span>Halvorsen</div>
  <div class="client" style="left:310px">Trevanta</div>
  <div class="client" style="left:519px">Olmstead</div>
  <div class="client" style="left:728px"><span class="mark"></span>Corvalis</div>
  <div class="client" style="left:938px"><span class="mark"></span>Pemberly</div>
  <span class="client-arrow" style="left:1130px"><svg width="8" height="10" viewBox="0 0 8 10"><path d="M1 0v10l7-5z" fill="#fff"/></svg></span>
</section>

<section class="newsletter">
  <svg class="envelope" width="42" height="34" viewBox="0 0 42 34"><rect x="2" y="6" width="36" height="26" fill="#fff"/><path d="M2 6l18 14L38 6" fill="none" stroke="#5b8fd6" stroke-width="2"/></svg>
  <span class="label">Newsletter Signup</span>
  <div class="email">Enter your email id</div>
  <div class="subscribe">SUBSCRIBE</div>
  <div class="follow">Follow Us : <span style="background:#3b5b9a"></span><span style="background:#2ba3e0"></span><span style="background:#1f7bb5"></span><span style="background:#d34836"></span></div>
</section>

<footer class="site-footer">
  <div class="footer-icons">
    <span style="background:var(--red)"><svg width="14" height="20" viewBox="0 0 14 20"><rect x="1" y="1" width="12" height="18" rx="2" fill="none" stroke="#fff" stroke-width="2"/><circle cx="7" cy="15" r="1.5" fill="#fff"/></svg></span>
    <span style="background:var(--blue)"><svg width="20" height="14" viewBox="0 0 20 14"><rect x="1" y="1" width="18" height="12" fill="#fff"/><path d="M1 1l9 7 9-7" fill="none" stroke="#5b8fd6" stroke-width="1.5"/></svg></span>
  </div>
  <div class="footer-brand">QRV Consulting</div>
  <nav class="footer-nav"><a>Home</a><a>About Us</a><a>Why QRV?</a><a>Our Process</a><a>Client</a><a>Contact Us</a></nav>
  <p class="copyright">Copyright © 2016 Qrvconsulting . All Rights Reserved</p>
</footer>

</body>
</html>
```